Tactical Supply Company needing memorable business card design

Our tactical supply comapny is in need of a new business card design that will set us apart from the amateurs. We sell tactical gear ranging from backpacks and range bags to apparel and other gear. We are looking for a sharp design that incorporates our logo, website, and name. Our colors are white, red, and black, or any combination of the three, preferably red and black.
I have attached our logo with our name underneath but I have also edited that design with the logo incorporated next to the name (attached).

Target Market(s)

Law enforcement, military, tactical

Industry/Entity Type

Business

Contact Information for Business Card

Include www.brindlequarry.example

Colors
000000
ec1f27
ffffff

Requirements
Must have
• Our name, logo, and website. This is intended to be a memorable simple card, no name, address, email, or phone number info is necessary. Designs that do include this additional info will still be considered if they are absolutely spectacular.
Should not have
• A standard template design, I can create that in my own on Cardomix. I am looking for a new, creative design that is completely unique to my company.

```html
<!DOCTYPE html>
<html lang="en">
<head>
<meta charset="utf-8">
<title>Brindle Quarry – Business Card</title>
<link rel="stylesheet" href="https://fonts.googleapis.com/css2?family=Exo+2:wght@400;500;800&display=swap">
<style>
  :root {
    --black: #000000;
    --plate-dark: #0b0b0c;
    --plate-mid: #1c1c1e;
    --red: #ec1f27;
    --red-deep: #a5121a;
    --white: #ffffff;
    --steel: #b9b9bc;
    --backdrop: #2a2a2c;
  }
  * { margin: 0; padding: 0; box-sizing: border-box; }
  html, body {
    width: 1200px; height: 1200px; overflow: hidden;
    background: var(--backdrop);
  }
  body { position: relative; font-family: "Exo 2", sans-serif; color: var(--white); }

  .business-card {
    position: absolute; left: 100px; top: 314px;
    width: 1000px; height: 572px;
    background: var(--black);
    overflow: hidden;
  }
  .tread-plate {
    position: absolute; left: 0; top: 0; width: 100%; height: 330px;
    background: radial-gradient(ellipse at 50% 40%, var(--plate-mid), var(--plate-dark) 75%);
  }
  .brand {
    position: absolute; left: 0; right: 0; top: 120px;
    display: flex; justify-content: center; align-items: center; gap: 26px;
  }
  .brand-dot {
    width: 70px; height: 70px; border-radius: 50%; background: var(--red);
  }
  .brand-name {
    font-weight: 800; font-size: 66px; letter-spacing: 3px;
    text-transform: uppercase; color: var(--white);
  }
  .steel-rule {
    position: absolute; left: 0; top: 330px; width: 100%; height: 10px;
    background: linear-gradient(180deg, #e6e6e8, var(--steel) 60%, #6d6d70);
  }
  .contact-band {
    position: absolute; left: 0; top: 340px; width: 100%; height: 232px;
    background: linear-gradient(180deg, var(--red-deep) 0%, var(--red) 45%, var(--red) 100%);
    border-top: 4px solid var(--red);
  }
  .contact-band::after {
    content: ""; position: absolute; inset: 10px 10px 10px 10px;
    border: 2px solid rgba(120, 0, 6, 0.55);
  }
  .person { position: absolute; left: 76px; top: 96px; }
  .person-name { font-size: 30px; font-weight: 500; }
  .person-role { font-size: 17px; color: rgba(255,255,255,0.6); margin-top: 2px; }

  .contact-list {
    position: absolute; left: 590px; top: 38px; list-style: none;
  }
  .contact-list li {
    display: flex; align-items: center; gap: 16px;
    font-size: 21px; line-height: 1; margin-bottom: 16px;
  }
  .contact-list svg { width: 24px; height: 24px; flex: none; }
</style>
</head>
<body>
  <article class="business-card">
    <div class="tread-plate" role="img" aria-label="Black diamond tread plate texture"></div>

    <div class="brand">
      <span class="brand-dot"></span>
      <span class="brand-name">Brindle Quarry</span>
    </div>

    <div class="steel-rule"></div>

    <section class="contact-band">
      <div class="person">
        <p class="person-name">Dale Harmon</p>
        <p class="person-role">Owner</p>
      </div>

      <ul class="contact-list">
        <li>
          <svg viewBox="0 0 24 24" aria-hidden="true">
            <circle cx="12" cy="12" r="10.5" fill="none" stroke="#fff" stroke-width="1.6"/>
            <path d="M8.5 7.5c.6-.6 1.4-.5 1.8.2l.8 1.4c.3.6.1 1.1-.4 1.5-.4.3-.4.7-.2 1.1.6 1 1.4 1.8 2.4 2.4.4.2.8.2 1.1-.2.4-.5.9-.7 1.5-.4l1.4.8c.7.4.8 1.2.2 1.8-1 1-2.5 1.3-3.9.6-2.2-1.1-4-2.9-5.1-5.1-.7-1.4-.4-2.9.4-3.9z" fill="#fff"/>
          </svg>
          <span>61 400 555 017</span>
        </li>
        <li>
          <svg viewBox="0 0 24 24" aria-hidden="true">
            <rect x="2.5" y="5.5" width="19" height="13" fill="none" stroke="#fff" stroke-width="1.6"/>
            <path d="M2.5 5.5 12 13l9.5-7.5" fill="none" stroke="#fff" stroke-width="1.6"/>
          </svg>
          <span>d.harmon@brindlequarry.example</span>
        </li>
        <li>
          <svg viewBox="0 0 24 24" aria-hidden="true">
            <circle cx="12" cy="12" r="10" fill="none" stroke="#fff" stroke-width="1.6"/>
            <ellipse cx="12" cy="12" rx="4.2" ry="10" fill="none" stroke="#fff" stroke-width="1.4"/>
            <path d="M2 12h20" stroke="#fff" stroke-width="1.4"/>
          </svg>
          <span>www.brindlequarry.example</span>
        </li>
      </ul>
    </section>
  </article>
</body>
</html>
```